Business Card Design Project

looking for a stylish and simple double sided business card.
I am an artist - specialising in fashion illustration, portraits and murals.
the front should be simply my name and tag:

D A V E R U
Living in colour

My preference is for a Black background with DAVERU in red or embossed.
Living in colour in White or multi-coloured.

the back will have detail:

Personalised Art
Portraits, Murals, Fashion Illustration

0487 312 560
daveru@daveru.com.au
www.daveru.com.au

Target Market(s)

Adults that are based in western speaking countries who have an appreciation for art and design. Portraits and wall art
Business owners who may need personalised all art for their business space. Murals and personalised canvass.
People in the fashion industry, who may require fashion illustrations.

Industry/Entity Type

Fashion

Requirements
Must have
• BOLD but simple at the same time, timeless modern element to it.
Nice to have
• simple lettering
Should not have
• Not too busy or wordy,

```html
<!DOCTYPE html>
<html lang="en">
<head>
<meta charset="utf-8">
<title>DAVERU – Business Card</title>
<link rel="stylesheet" href="https://fonts.googleapis.com/css2?family=Oswald:wght@500&family=Roboto:wght@400&family=Kaushan+Script&display=swap">
<style>
  :root {
    --backdrop: #d9d9d9;
    --card-black: #1c1c1e;
    --card-black-glow: #3b3b3e;
    --card-white: #ffffff;
    --service-red: #e0202e;
    --ink: #1f1f1f;
    --paper: #f2f2f2;
  }
  * { box-sizing: border-box; margin: 0; padding: 0; }
  html, body {
    width: 1200px; height: 1013px; overflow: hidden;
    background: var(--backdrop);
  }
  .sheet {
    width: 1200px; height: 1013px;
    display: flex; flex-direction: column; align-items: center; justify-content: center;
    gap: 40px;
  }
  .card {
    position: relative;
    width: 740px; height: 452px;
    overflow: hidden;
    box-shadow: 0 6px 18px rgba(0,0,0,0.18);
  }

  /* Front */
  .card-front {
    background: radial-gradient(ellipse at 50% 45%, var(--card-black-glow) 0%, var(--card-black) 65%);
    display: flex; flex-direction: column; align-items: center; justify-content: center;
  }
  .brand-name {
    font-family: "Roboto", sans-serif;
    font-weight: 400;
    font-size: 64px;
    line-height: 1;
    letter-spacing: 14px;
    padding-left: 14px;
    color: var(--paper);
  }
  .brand-tagline {
    margin-top: 28px;
    font-family: "Roboto", sans-serif;
    font-weight: 400;
    font-size: 15px;
    letter-spacing: 6px;
    padding-left: 6px;
    text-transform: uppercase;
    color: var(--paper);
    opacity: 0.8;
  }

  /* Back */
  .card-back { background: var(--card-white); }
  .back-band {
    position: absolute; left: 0; top: 0;
    width: 100%; height: 56px;
    background: linear-gradient(180deg, #151517, #2a2a2d);
  }
  .services {
    position: absolute; left: 0; right: 0; top: 150px;
    text-align: center;
    font-family: "Oswald", sans-serif;
    font-weight: 500;
    font-size: 27px;
    letter-spacing: 0.3px;
    color: var(--service-red);
    text-transform: uppercase;
  }
  .services .sep { color: var(--ink); margin: 0 6px; }
  .contact-list {
    position: absolute; left: 44px; top: 268px;
    list-style: none;
    font-family: "Roboto", sans-serif;
    font-size: 17px;
    color: var(--ink);
  }
  .contact-list li {
    display: flex; align-items: center; gap: 10px;
    height: 27px;
  }
  .contact-list svg { width: 14px; height: 14px; flex: none; }
  .signature {
    position: absolute; right: 90px; bottom: 52px;
    text-align: center;
  }
  .signature-text {
    font-family: "Kaushan Script", cursive;
    font-size: 30px;
    color: var(--ink);
  }
  .signature-line {
    display: block;
    width: 220px; height: 3px;
    margin-top: 2px;
    background: var(--ink);
    border-radius: 2px;
  }
</style>
</head>
<body>
<main class="sheet">
  <section class="card card-front" aria-label="Card front">
    <h1 class="brand-name">DAVERU</h1>
    <p class="brand-tagline">Living in Colour</p>
  </section>

  <section class="card card-back" aria-label="Card back">
    <div class="back-band"></div>
    <p class="services">Portraits<span class="sep">•</span>Murals<span class="sep">•</span>Fashion Illustration</p>
    <ul class="contact-list">
      <li>
        <svg viewBox="0 0 14 14" aria-hidden="true"><rect x="3.5" y="0.5" width="7" height="13" rx="1.2" fill="none" stroke="#1f1f1f" stroke-width="1.4"/><rect x="5" y="2.5" width="4" height="7.5" fill="#1f1f1f"/></svg>
        <span>0487 312 560</span>
      </li>
      <li>
        <svg viewBox="0 0 14 14" aria-hidden="true"><rect x="0.5" y="2.5" width="13" height="9" fill="#1f1f1f"/><path d="M0.5 2.5 L7 8 L13.5 2.5" fill="none" stroke="#fff" stroke-width="1"/></svg>
        <span>daveru@daveru.com.au</span>
      </li>
      <li>
        <svg viewBox="0 0 14 14" aria-hidden="true"><circle cx="7" cy="7" r="6.2" fill="none" stroke="#1f1f1f" stroke-width="1.3"/><ellipse cx="7" cy="7" rx="2.6" ry="6.2" fill="none" stroke="#1f1f1f" stroke-width="1.1"/><line x1="0.8" y1="7" x2="13.2" y2="7" stroke="#1f1f1f" stroke-width="1.1"/></svg>
        <span>www.daveru.com.au</span>
      </li>
    </ul>
    <div class="signature">
      <p class="signature-text">Personalised Artist</p>
      <span class="signature-line"></span>
    </div>
  </section>
</main>
</body>
</html>
```